Quorvan Stationery Design Project

We need stationary design that goes with the attached logo. We have logo in two different versions. One in Red/Black and the other in Blue/Green. Red/Black is going to be our primary color and we are planning to use Blue/Green occasionally as necessary.

So we need stationary design in both color combinations. Maybe you can work with Red/Black first and once we decide on the design, then you can show the Blue/Green variation.

Please see the attached png and psd files for logo.

Target Market(s)

IT departments of Medium size Enterprises.

Industry/Entity Type

Work

Requirements
Must have
• -Letter head
-Cover page design for white papers and articles that are going to publish
-Business Card
-Envelope design
Nice to have
• - High level design template that we can follow for our internal web applications

```html
<!DOCTYPE html>
<html lang="en">
<head>
<meta charset="utf-8">
<title>Quorvan Stationery</title>
<link href="https://fonts.googleapis.com/css2?family=Arimo:wght@400;700&display=swap" rel="stylesheet">
<style>
:root{
  --backdrop:#e9e9e9;
  --paper:#f7f7f6;
  --ink:#231f20;
  --muted:#555;
  --rule:#9a9a9a;
  --cell:#e2e2e2;
  --brand-red:#d2232a;
}
*{box-sizing:border-box;margin:0;padding:0}
html,body{width:1200px;height:815px;overflow:hidden}
body{background:var(--backdrop);font-family:"Arimo",Arial,sans-serif;color:var(--ink);position:relative}
.sheet{position:absolute;top:72px;width:482px;height:681px;background:var(--paper);box-shadow:0 2px 8px rgba(0,0,0,.12)}
.sheet--letterhead{left:80px}
.sheet--fax{left:638px}
.brand{position:absolute;left:41px;top:36px;display:flex;align-items:center;gap:8px}
.brand__square{width:26px;height:26px;background:var(--brand-red)}
.brand__name{font-size:17px;font-weight:700;letter-spacing:3px;color:var(--ink)}
.footer__rule{position:absolute;left:40px;right:40px;top:641px;height:1.5px;background:var(--brand-red)}
.footer__contact{position:absolute;left:40px;top:648px;font-size:7px;line-height:9px;color:var(--muted)}
.footer__contact b{color:var(--brand-red);font-weight:700}
.footer__web{position:absolute;right:40px;top:650px;font-size:7px;color:var(--muted)}
.footer__web b{color:var(--brand-red);font-weight:700}
.fax-title{position:absolute;right:40px;top:24px;font-size:62px;line-height:62px;font-weight:400;color:var(--ink)}
.fax-details{position:absolute;left:41px;top:115px;width:402px;border-collapse:collapse;font-size:7px}
.fax-details td{height:14px;border:1px solid var(--rule);padding:0 4px;color:var(--muted);font-weight:700}
.fax-details .label{width:43px;background:var(--cell)}
.fax-details .field{width:158px;background:var(--paper)}
.fax-flags{position:absolute;left:41px;top:199px;width:402px;height:14px;display:flex;border:1px solid var(--rule);background:var(--cell);font-size:7px;font-weight:700;color:var(--muted)}
.fax-flags span{flex:1;display:flex;align-items:center;justify-content:center;gap:3px;border-right:1px solid var(--rule)}
.fax-flags span:last-child{border-right:none}
.fax-flags i{width:5px;height:5px;border:1px solid var(--muted);display:inline-block}
.fax-comments{position:absolute;left:41px;top:213px;width:402px;height:408px;border:1px solid var(--rule);border-top:none}
.fax-comments p{text-align:center;margin-top:12px;font-size:7px;color:var(--muted)}
</style>
</head>
<body>

<section class="sheet sheet--letterhead">
  <div class="brand"><span class="brand__square"></span><span class="brand__name">QUORVAN</span></div>
  <div class="footer__rule"></div>
  <p class="footer__contact">2400 Harlow Avenue, Suite 310, Dayton, OH 45402-1180<br><b>T:</b> (555) 201-4870 · <b>F:</b> (555) 201-4871 · <b>E:</b> info@quorvan.com</p>
  <p class="footer__web">www.<b>quorvan</b>.com</p>
</section>

<section class="sheet sheet--fax">
  <div class="brand"><span class="brand__square"></span><span class="brand__name">QUORVAN</span></div>
  <h1 class="fax-title">FAX</h1>
  <table class="fax-details">
    <tr><td class="label">To:</td><td class="field"></td><td class="label">From:</td><td class="field"></td></tr>
    <tr><td class="label">Fax:</td><td class="field"></td><td class="label">Pages:</td><td class="field"></td></tr>
    <tr><td class="label">Phone:</td><td class="field"></td><td class="label">Date:</td><td class="field"></td></tr>
    <tr><td class="label">Re:</td><td class="field"></td><td class="label">CC:</td><td class="field"></td></tr>
  </table>
  <div class="fax-flags">
    <span><i></i>Urgent</span>
    <span><i></i>For Review</span>
    <span><i></i>Please Comment</span>
    <span><i></i>Please Reply</span>
    <span><i></i>Confidential</span>
  </div>
  <div class="fax-comments"><p>COMMENTS:</p></div>
  <div class="footer__rule"></div>
  <p class="footer__contact">2400 Harlow Avenue, Suite 310, Dayton, OH 45402-1180<br><b>T:</b> (555) 201-4870 · <b>F:</b> (555) 201-4871 · <b>E:</b> info@quorvan.com</p>
  <p class="footer__web">www.<b>quorvan</b>.com</p>
</section>

</body>
</html>
```